5x5 Pop Up Display, Company Logo With Text and Graphics for Tradeshow Display

Design for a 5ft x 5ft pop up trade show display that will sit on top of a table. I usually prefer clean, somewhat minimalist designs. We are a food service company but it's not a requirement to have photos of food. Design elements should compliment the table cloth that we have for the booth. The below may be included depending on the design aesthetic.
Service Provided: Daily Meal Service, Kitchen Management
"Nationwide Footprint"
"Grassroots Service"
"Fresh Scratch Cooking"
"Custom Menus"
"Made To Order Meals"

```html
<!DOCTYPE html>
<html lang="en">
<head>
<meta charset="utf-8">
<title>Hale Hearth – Tradeshow Display</title>
<link href="https://fonts.googleapis.com/css2?family=PT+Serif:wght@700&family=Poppins:wght@500&display=swap" rel="stylesheet">
<style>
  :root {
    --forest: #2f4a2c;
    --glow: #9db44f;
    --cream: #f3e1a6;
    --white: #ffffff;
    --ink: #111111;
    --lime: #8cc63f;
    --field-light: #86b83c;
    --field-dark: #2e8a24;
    --rule-gold: #f7d27a;
    --page: #ffffff;
  }
  * { margin: 0; padding: 0; box-sizing: border-box; }
  html, body { width: 1200px; height: 3106px; overflow: hidden; background: var(--page); }
  body { position: relative; font-family: "PT Serif", Georgia, serif; }

  .backdrop-panel {
    position: absolute; left: 100px; top: 765px; width: 1000px; height: 1000px;
    background:
      radial-gradient(ellipse 440px 340px at 50% 100%, var(--glow) 0%, rgba(157,180,79,0.55) 35%, rgba(47,74,44,0) 100%),
      var(--forest);
    box-shadow: 0 10px 30px rgba(0,0,0,0.25);
    color: var(--white);
    text-align: center;
  }

  .brand-name {
    position: absolute; left: 0; right: 0;
    font-family: "PT Serif", Georgia, serif; font-weight: 700;
    text-transform: uppercase; line-height: 1; white-space: nowrap;
    display: flex; justify-content: center; align-items: center; gap: 22px;
  }
  .brand-name .name-dot {
    width: 26px; height: 26px; border-radius: 50%; background: var(--lime); flex: none;
  }
  .backdrop-panel .brand-name { top: 100px; font-size: 84px; letter-spacing: 2px; }

  .headline {
    position: absolute; left: 0; right: 0; top: 236px;
    font-family: "PT Serif", Georgia, serif; font-weight: 700;
    font-size: 112px; line-height: 98px; text-transform: uppercase; letter-spacing: 1px;
  }
  .headline span { display: block; }
  .headline .accent { color: var(--cream); }

  .service-row {
    position: absolute; left: 78px; right: 70px; top: 565px;
    list-style: none;
    display: flex; justify-content: space-between; align-items: center;
    font-family: "Poppins", Arial, sans-serif; font-weight: 500;
    font-size: 27px; line-height: 1.18; text-align: left;
  }
  .service { display: flex; align-items: center; gap: 16px; }
  .service svg { width: 76px; height: 70px; flex: none; }

  .table-banner {
    position: absolute; left: 110px; top: 1865px; width: 995px; height: 475px;
    background: var(--white); overflow: hidden;
    box-shadow: 0 10px 30px rgba(0,0,0,0.22);
  }
  .table-banner .brand-name {
    top: 170px; font-size: 96px; color: var(--ink); letter-spacing: 2px;
  }
  .table-banner .name-dot { width: 30px; height: 30px; background: var(--field-dark); }
  .table-banner .base-band {
    position: absolute; left: 0; right: 0; bottom: 0; height: 110px;
    background: linear-gradient(90deg, var(--field-light), var(--field-dark));
    border-top: 10px solid var(--rule-gold);
  }
</style>
</head>
<body>

<section class="backdrop-panel" aria-label="Backdrop panel">
  <div class="brand-name">Hale Hearth<span class="name-dot"></span></div>

  <h1 class="headline">
    <span>Fresh</span>
    <span>Scratch</span>
    <span class="accent">Cooking</span>
  </h1>

  <ul class="service-row">
    <li class="service">
      <svg viewBox="0 0 80 74" fill="none" stroke="#fff" stroke-width="4">
        <circle cx="46" cy="32" r="24"/><circle cx="34" cy="32" r="26"/><circle cx="34" cy="32" r="17"/>
        <line x1="18" y1="68" x2="52" y2="68" stroke-linecap="round"/>
      </svg>
      <span>Daily Meal<br>Service</span>
    </li>
    <li class="service">
      <svg viewBox="0 0 80 74" fill="#fff">
        <circle cx="40" cy="34" r="10"/><path d="M22 70c0-14 8-22 18-22s18 8 18 22z"/>
        <circle cx="16" cy="44" r="7"/><path d="M2 72c0-10 6-16 14-16s12 4 12 10v6z"/>
        <circle cx="64" cy="44" r="7"/><path d="M78 72c0-10-6-16-14-16s-12 4-12 10v6z"/>
        <rect x="52" y="4" width="6" height="22" rx="3" transform="rotate(40 55 15)"/>
      </svg>
      <span>Staffing &amp; Kitchen<br>Management</span>
    </li>
    <li class="service">
      <svg viewBox="0 0 80 74" fill="none" stroke="#fff" stroke-width="4">
        <circle cx="40" cy="42" r="24"/><ellipse cx="40" cy="42" rx="10" ry="24"/>
        <line x1="16" y1="42" x2="64" y2="42"/><line x1="20" y1="30" x2="60" y2="30"/><line x1="20" y1="54" x2="60" y2="54"/>
      </svg>
      <span>Nationwide<br>Footprint</span>
    </li>
  </ul>
</section>

<section class="table-banner" aria-label="Table cover">
  <div class="brand-name">Hale Hearth<span class="name-dot"></span></div>
  <div class="base-band"></div>
</section>

</body>
</html>
```